Create a Poster Campaign for a Zurich-based Crowdfinancing Startup

Company: Tamsorelia GmbH (tmsq.ch)
Campaign: First major marketing push
Scope: Billboard posters

Company description:
Tamsorelia GmbH is a crowdfinancing platform, where people and businesses needing money can raise funds in three different ways: 1. Crowdlending (borrowing and paying interest), 2. Crowdfactoring for businesses (pre-financing an open invoice), 3. Crowdfunding (rewards-based funding). What Tamsorelia from the competitors differentiates is that borrowers can borrow at their own conditions (amount, duration up to 5 years, and interest rate).
MORE INFO: www.tmsq.ch

We are also changing website colours to blue away from brown.

Need:
We need to attract more users to the platform and because we only operate in Switzerland, a poster campaign is meant to create awareness of our brand and services.

We need 2 posters designs in F 200 and F 24 Large Format (Here is a tool to see poster sizes (https://booking.vorlandposter.ch/en/poster-design-tips-and-checklist)

Notes:
We would like to use tmsq.ch as the name and address of the platform. We do not want plant motifs (growth of a plant from dirt, or money growing).

Slogan Ideas:
Too much money? Not enough money? Come to TMSQ.

We’ve got your next loan.

Balanced for borrowers and lenders. <— potentially a secondary text block

Target Market(s)

People who need money (businesses and private people) as well as people and businesses looking to invest money. It needs to speak to both.

Industry/Entity Type

Financial

Font styles to use
Serif
Sans Serif

Colors
0355a3
3276b5
85acd3
cedeed

Requirements
Must have
• Message and headline: must get across in 1–2 seconds, be catchy and easy to grasp
• Few words: maximum of ten
• Font size should make text readable up to ten metres
• High contrast dark on light and complementary colours are easiest to take in
• Logo must be clearly recognizable.
• Elements essential to the image, such as texts, should be placed at least 6 cm – in the case of F12 and F24 – and 4 cm – in the case of F4 and F200 formats – from the edge at the top, bottom and sides (this is mandatory in the case of posters placed in light boxes).
Nice to have
• Brelt and Lumen Ostrak have done some creative posters.
Should not have
• No plant images

```html
<!DOCTYPE html>
<html lang="en">
<head>
<meta charset="utf-8">
<title>Tamsorelia – Poster</title>
<link href="https://fonts.googleapis.com/css2?family=Oswald:wght@500;600;700&family=Catamaran:wght@400;500;600;700&display=swap" rel="stylesheet">
<style>
  :root {
    --navy: #0b4a8e;
    --navy-deep: #073f7d;
    --cyan: #19c6f3;
    --white: #ffffff;
    --ink: #3d3d3d;
    --skin: #c9a27e;
    --shirt: #b88a60;
  }
  * { margin: 0; padding: 0; box-sizing: border-box; }
  html, body { width: 869px; height: 1200px; overflow: hidden; background: #eeeeee; }
  .poster {
    position: relative; width: 869px; height: 1200px; overflow: hidden;
    background: linear-gradient(180deg, var(--navy-deep) 0%, var(--navy) 60%);
    font-family: "Catamaran", sans-serif;
  }
  .headline-block { position: absolute; left: 0; right: 0; text-align: center; }
  .teaser {
    top: 28px; font-family: "Oswald", sans-serif; font-weight: 600;
    font-size: 44px; line-height: 56px; color: var(--cyan); word-spacing: 6px;
  }
  .main-title {
    top: 84px; font-family: "Oswald", sans-serif; font-weight: 700;
    font-size: 78px; line-height: 90px; color: var(--white);
  }
  .subtitle {
    top: 170px; font-weight: 700; font-size: 48px; line-height: 60px;
    color: var(--cyan); letter-spacing: -0.5px;
  }
  .tagline {
    top: 228px; font-family: "Oswald", sans-serif; font-weight: 500;
    font-size: 28px; line-height: 38px; color: var(--white);
  }
  .brand {
    position: absolute; left: 50px; top: 318px; display: flex; align-items: center; gap: 14px;
  }
  .brand-dot { width: 64px; height: 64px; border-radius: 50%; background: var(--white); }
  .brand-name {
    font-family: "Oswald", sans-serif; font-weight: 600; font-size: 40px; color: var(--white);
  }
  .hero-photo {
    position: absolute; left: 101px; top: 286px; width: 587px; height: 501px;
    background: radial-gradient(ellipse at 55% 60%, var(--shirt) 0%, #9c734f 45%, rgba(11,74,142,0) 72%);
  }
  .waves { position: absolute; inset: 0; }
  .burst { position: absolute; left: 627px; top: 263px; width: 200px; height: 200px; }
  .burst-label {
    position: absolute; left: 627px; top: 263px; width: 200px; height: 200px;
    display: flex; align-items: center; justify-content: center; text-align: center;
    font-family: "Oswald", sans-serif; font-weight: 600; font-size: 31px; line-height: 38px;
    color: var(--white);
  }
  .intro, .differentiator {
    position: absolute; left: 40px; right: 40px; text-align: center;
    font-size: 17px; line-height: 22px; color: var(--ink); font-weight: 500; letter-spacing: -0.3px;
  }
  .intro { top: 801px; }
  .differentiator { top: 1057px; }
  .service {
    position: absolute; top: 877px; width: 170px; height: 170px; margin-left: -85px;
  }
  .service-disc {
    position: absolute; left: 0; top: 0; width: 170px; height: 170px; border-radius: 50%;
    background: var(--navy); border: 5px solid var(--cyan);
    display: flex; flex-direction: column; align-items: center; justify-content: center;
    padding: 18px 20px 0; text-align: center; color: var(--white);
  }
  .service-title { font-family: "Oswald", sans-serif; font-weight: 600; font-size: 23px; line-height: 28px; }
  .service-note { font-size: 16px; line-height: 19px; font-weight: 400; }
  .service-number {
    position: absolute; left: 57px; top: -24px; width: 56px; height: 56px; border-radius: 50%;
    background: var(--cyan); color: var(--white); text-align: center;
    font-family: "Oswald", sans-serif; font-weight: 600; font-size: 34px; line-height: 54px;
  }
  .service--lending { left: 166px; }
  .service--factoring { left: 433px; }
  .service--funding { left: 707px; }
  .web-address {
    position: absolute; left: 0; right: 0; top: 1142px; text-align: center;
    font-weight: 600; font-size: 28px; letter-spacing: 6px; color: var(--white);
  }
</style>
</head>
<body>
<main class="poster">
  <div class="hero-photo" role="img" aria-label="Photo of a puzzled man in glasses, shirt and tie, shrugging with one open hand and holding banknotes in the other"></div>

  <svg class="waves" width="869" height="1200" viewBox="0 0 869 1200" aria-hidden="true">
    <path d="M0,720 Q434,800 869,716 L869,1200 L0,1200 Z" fill="var(--cyan)"/>
    <path d="M0,738 Q434,798 869,732 L869,1200 L0,1200 Z" fill="var(--white)"/>
    <path d="M0,1170 Q434,1082 869,1170 L869,1200 L0,1200 Z" fill="var(--cyan)"/>
  </svg>

  <p class="headline-block teaser">Too much MONEY? &nbsp;Not enough MONEY?</p>
  <h1 class="headline-block main-title">Come to TMSQ</h1>
  <p class="headline-block subtitle">We’ve got your next loan</p>
  <p class="headline-block tagline">Balanced for borrowers and lenders</p>

  <div class="brand">
    <span class="brand-dot"></span>
    <span class="brand-name">Tamsorelia</span>
  </div>

  <svg class="burst" viewBox="-100 -100 200 200" aria-hidden="true">
    <polygon fill="var(--cyan)" points="98,0 83,13.1 93.2,30.3 74.8,38.1 79.3,57.6 59.4,59.4 57.6,79.3 38.1,74.8 30.3,93.2 13.1,83 0,98 -13.1,83 -30.3,93.2 -38.1,74.8 -57.6,79.3 -59.4,59.4 -79.3,57.6 -74.8,38.1 -93.2,30.3 -83,13.1 -98,0 -83,-13.1 -93.2,-30.3 -74.8,-38.1 -79.3,-57.6 -59.4,-59.4 -57.6,-79.3 -38.1,-74.8 -30.3,-93.2 -13.1,-83 0,-98 13.1,-83 30.3,-93.2 38.1,-74.8 57.6,-79.3 59.4,-59.4 79.3,-57.6 74.8,-38.1 93.2,-30.3 83,-13.1"/>
  </svg>
  <p class="burst-label">CONTACT<br>US TODAY</p>

  <p class="intro">Tamsorelia GmbH is a crowdfinancing platform, where people and businesses needing<br>money can raise funds in three different ways:</p>

  <section class="service service--lending">
    <div class="service-disc">
      <span class="service-title">Crowdlending</span>
      <span class="service-note">(borrowing and paying interest),</span>
    </div>
    <span class="service-number">1</span>
  </section>

  <section class="service service--factoring">
    <div class="service-disc">
      <span class="service-title">Crowdfactoring</span>
      <span class="service-note">for businesses (pre-financing an open invoice),</span>
    </div>
    <span class="service-number">2</span>
  </section>

  <section class="service service--funding">
    <div class="service-disc">
      <span class="service-title">Crowdfunding</span>
      <span class="service-note">(rewards-<br>based funding).</span>
    </div>
    <span class="service-number">3</span>
  </section>

  <p class="differentiator">What Tamsorelia from the competitors differentiates is that borrowers can borrow at<br>their own conditions (amount, duration up to 5 years, and interest rate).</p>

  <p class="web-address">www.tmsq.ch</p>
</main>
</body>
</html>
```